KLT Proposal Flyer Document

Hi Marketing Team, Require this MS Word doc in a professional proposal flyer format that I can use for proposal to customers, it needs to reflect the KLT Business and Culture, which is a HR Consultancy firm so lots pics of people welcoming, reading at meetings ect, so its people and business focused. Pls note the document needs to be able to be interacted with as well as saved and emailed to clients in PDF format, so pls keep this in mind when doing the design. Thanks very much

Target Market(s)

HR Managers, Global Business Leaders and Decision Makers

Colors
ec1f27

Requirements
Must have
• Professional look

```html
<!DOCTYPE html>
<html lang="en">
<head>
<meta charset="utf-8">
<title>KLT Proposal Document</title>
<link rel="stylesheet" href="https://fonts.googleapis.com/css2?family=Montserrat:wght@400;500;600;700;800&family=Tinos:wght@700&display=swap">
<style>
:root{
  --navy:#16467f;
  --navy-deep:#0e3566;
  --red:#ec1f27;
  --orange:#f1592a;
  --orange-hot:#e9402a;
  --ink:#2b2b2b;
  --rule:#c9c9c9;
  --row:#e4e4e4;
  --canvas:#ffffff;
}
*{box-sizing:border-box;margin:0;padding:0}
html,body{width:1200px;height:3691px;overflow:hidden;background:var(--canvas)}
body{position:relative;font-family:"Montserrat",Arial,sans-serif;color:var(--ink)}
.page{position:absolute;left:216px;width:770px;height:1087px;background:#fff;box-shadow:0 0 6px rgba(0,0,0,.35);overflow:hidden}
.page--one{top:159px}.page--two{top:1320px}.page--three{top:2480px}
.page-frame{position:absolute;left:0;top:0;width:770px;height:1087px}
.brand{position:absolute;left:50px;top:26px;display:flex;align-items:center;gap:10px}
.brand-dot{width:46px;height:46px;border-radius:50%;background:var(--red)}
.brand-name{font-weight:800;font-size:58px;line-height:1;color:var(--red);letter-spacing:1px}
.brand-tag{position:absolute;left:50px;top:86px;font-weight:700;font-size:12.5px;color:var(--red);letter-spacing:.4px}
.page-number{position:absolute;right:66px;bottom:20px;color:#fff;font-weight:600;font-size:22px}
.block{position:absolute;left:52px;width:666px;font-size:11.5px;line-height:1.45}
.heading{font-weight:700;font-size:15px;color:var(--navy-deep);letter-spacing:.3px}
.pillars{position:absolute;left:52px;top:158px;display:flex;gap:8px}
.pillar{width:217px;height:149px;display:flex;flex-direction:column}
.pillar-art{flex:1;background:linear-gradient(90deg,var(--orange-hot),var(--orange));border-radius:12px 12px 0 0}
.pillar-label{height:37px;background:var(--navy);font-family:"Tinos",serif;font-weight:700;font-size:19px;color:#fff;text-align:center;line-height:39px}
.pillar-label span{color:var(--orange)}
.offers{list-style:none}
.offers li{position:absolute;left:0;padding-left:28px;width:666px}
.tick{position:absolute;left:0;top:1px;width:13px;height:13px}
.data{position:absolute;left:52px;width:666px;border-collapse:collapse;font-size:11.5px}
.data th{background:var(--navy);color:#fff;font-weight:600;text-align:left;padding:0 26px;height:36px}
.data thead tr th:first-child{border-top-left-radius:14px}
.data thead tr th:last-child{border-top-right-radius:14px}
.data td{border:1px solid var(--rule);height:30px;padding:0 26px}
.data--summary td{background:var(--row);border:none;height:36px;font-weight:600}
.data--summary td.note{font-weight:400;font-size:10.5px;line-height:1.2}
.steps{list-style:none}
.steps li{position:absolute;left:0;padding-left:24px;width:666px}
.steps b{position:absolute;left:0;font-size:13px}
.lifecycle{position:absolute;left:52px;top:494px;width:663px;height:395px;background:radial-gradient(circle at 62% 52%,#fbe4c7 0,#f7c79a 18%,#e9eef2 34%,#f4f4f4 60%)}
.data--compact th{font-size:10.5px;padding:0 12px;line-height:1.15}
.data--compact td{padding:0 12px;font-size:10.5px}
</style>
</head>
<body>

<section class="page page--one">
  <svg class="page-frame" viewBox="0 0 770 1087" aria-hidden="true">
    <defs><linearGradient id="band1" x1="0" x2="1"><stop offset="0" stop-color="#0e3566"/><stop offset="1" stop-color="#1c5392"/></linearGradient></defs>
    <path d="M0 0H770V40H575C480 40 460 118 370 118H0Z" fill="url(#band1)"/>
    <path d="M0 1061H500C555 1061 555 1026 615 1026H770V1087H0Z" fill="url(#band1)"/>
  </svg>
  <div class="brand"><span class="brand-dot"></span><span class="brand-name">KLT</span></div>
  <div class="brand-tag">KESTREL LANE TALENT</div>

  <div class="pillars">
    <div class="pillar"><div class="pillar-art" role="img" aria-label="Bonsai tree icon for purpose"></div><div class="pillar-label">OUR <span>PURPOSE</span></div></div>
    <div class="pillar"><div class="pillar-art" role="img" aria-label="Guiding star icon for vision"></div><div class="pillar-label">OUR <span>VISION</span></div></div>
    <div class="pillar"><div class="pillar-art" role="img" aria-label="Compass icon for strategy"></div><div class="pillar-label">OUR <span>STRATEGY</span></div></div>
  </div>

  <p class="block" style="top:347px">( The above pictures idea only need to be change to perhaps consulting people pics first or business theme)&nbsp; HR Strategy | HR Operations | HR Projects | Business Solutions.</p>
  <h2 class="block heading" style="top:404px">OUR VISION:</h2>
  <p class="block" style="top:432px">Build high performing HR Capital Talent and Solutions for local and global business leaders for current and future business needs.</p>
  <p class="block" style="top:476px">Our Purpose is to provide HR Strategy, Hands on HR Operational Services and deliver timely Projects to develop, nurture talent and find the best solutions for global business leaders.</p>
  <h2 class="block heading" style="top:531px">OUR STRATEGY:</h2>
  <p class="block" style="top:559px">To differentiate ourselves based on having a positive impact and providing an exceptional client care experience.</p>
  <h2 class="block heading" style="top:611px">SERVICE OFFERINGS:</h2>
  <ul class="block offers" style="top:0">
    <li style="top:644px"><svg class="tick" viewBox="0 0 13 13"><rect x=".7" y="1.7" width="10.6" height="10.6" fill="none" stroke="#ec1f27" stroke-width="1.4"/><path d="M3 6.5l3 3 6.5-8" fill="none" stroke="#ec1f27" stroke-width="1.8"/></svg># Consult with Senior Leaders on critical business issues and find the best solutions.</li>
    <li style="top:678px"><svg class="tick" viewBox="0 0 13 13"><rect x=".7" y="1.7" width="10.6" height="10.6" fill="none" stroke="#ec1f27" stroke-width="1.4"/><path d="M3 6.5l3 3 6.5-8" fill="none" stroke="#ec1f27" stroke-width="1.8"/></svg># Work with the business to Build Strategies across, Employee Branding # Employee Engagement # Performance Management # Talent Management # Best Practices to accelerate business growth.</li>
    <li style="top:729px"><svg class="tick" viewBox="0 0 13 13"><rect x=".7" y="1.7" width="10.6" height="10.6" fill="none" stroke="#ec1f27" stroke-width="1.4"/><path d="M3 6.5l3 3 6.5-8" fill="none" stroke="#ec1f27" stroke-width="1.8"/></svg># Recommend solutions and tools to add structure to the Human Resources function to create employee engagement, positive communications and enable businesses to scale.</li>
    <li style="top:780px"><svg class="tick" viewBox="0 0 13 13"><rect x=".7" y="1.7" width="10.6" height="10.6" fill="none" stroke="#ec1f27" stroke-width="1.4"/><path d="M3 6.5l3 3 6.5-8" fill="none" stroke="#ec1f27" stroke-width="1.8"/></svg># Support business leaders in HR Projects aligned to business improvement and growth.</li>
  </ul>
  <p class="block" style="top:832px">Human Resources Strategy, HR Operations and HR Projects</p>
  <table class="data data--summary" style="top:866px">
    <thead><tr><th style="width:190px">Version</th><th style="width:190px">Issue Date</th><th>Project</th></tr></thead>
    <tbody><tr><td>1.0</td><td>2020</td><td class="note">Consultation with Business.<br>Sample Project Framework.</td></tr></tbody>
  </table>
  <p class="block" style="top:979px;font-weight:500">1. Project Scope</p>
  <div class="page-number">01</div>
</section>

<section class="page page--two">
  <svg class="page-frame" viewBox="0 0 770 1087" aria-hidden="true">
    <defs><linearGradient id="band2" x1="0" x2="1"><stop offset="0" stop-color="#0e3566"/><stop offset="1" stop-color="#1c5392"/></linearGradient></defs>
    <path d="M0 0H770V40H575C480 40 460 118 370 118H0Z" fill="url(#band2)"/>
    <path d="M0 1061H500C555 1061 555 1026 615 1026H770V1087H0Z" fill="url(#band2)"/>
  </svg>
  <div class="brand"><span class="brand-dot"></span><span class="brand-name">KLT</span></div>
  <div class="brand-tag">KESTREL LANE TALENT</div>

  <p class="block" style="top:152px">Initial communication to understand current HR Framework in place or leverage from Regional/Global Head Office.Understanding the current HR Model in place and Assessment of current HR Practices across the HR Employee Lifecycle and key business strategies and goals currently in place.</p>
  <p class="block" style="top:223px;font-weight:700;font-size:10px">The main areas of focus is an initial conversation regards to understanding of the current HR Landscape, current Model in Place, current practices, systems and policies across the organization.</p>
  <ol class="block steps" style="top:0">
    <li style="top:270px"><b>1)</b>Review and understand current HR Practices, culture, values and work environment. Style of business structure and leadership in place currently.</li>
    <li style="top:317px"><b>2)</b>Current HR Model in place, current systems, practices across the Employee Lifecycle as aligned to Principles of Fair Employment Practices, NFEP Guidelines and The Open Workplace Model as a reference model.</li>
    <li style="top:370px"><b>3)</b>Key Business Goals, Strategy, Plans and Priorities current and the future.</li>
    <li style="top:399px"><b>4)</b>Gain an understanding of current Employee Pulse and any Recent Surveys</li>
    <li style="top:427px"><b>5)</b>Gain an understanding of current Safety Strategy that is in place with Covid-19, review policies to date.</li>
  </ol>
  <div class="lifecycle" role="img" aria-label="Employee lifecycle infographic: attraction, recruitment, onboarding, development, retention and separation around engagement"></div>
  <p class="block" style="top:935px">" Hire, Inspire, Retire" Approach Reference: Adopted from the Open Workplace Employee LifeCycle Model, Author: Helen Marsh.</p>
  <div class="page-number">02</div>
</section>

<section class="page page--three">
  <svg class="page-frame" viewBox="0 0 770 1087" aria-hidden="true">
    <defs><linearGradient id="band3" x1="0" x2="1"><stop offset="0" stop-color="#0e3566"/><stop offset="1" stop-color="#1c5392"/></linearGradient></defs>
    <path d="M0 0H770V40H575C480 40 460 118 370 118H0Z" fill="url(#band3)"/>
    <path d="M0 1061H500C555 1061 555 1026 615 1026H770V1087H0Z" fill="url(#band3)"/>
  </svg>
  <div class="brand"><span class="brand-dot"></span><span class="brand-name">KLT</span></div>
  <div class="brand-tag">KESTREL LANE TALENT</div>

  <p class="block" style="top:158px;font-weight:600">2.Project Resources</p>
  <table class="data" style="top:194px">
    <thead><tr><th style="width:196px">Resources</th><th style="width:236px;text-align:center">Value Add Position</th><th>Years of Experience</th></tr></thead>
    <tbody><tr><td></td><td></td><td></td></tr><tr><td></td><td></td><td></td></tr><tr><td></td><td></td><td></td></tr><tr><td></td><td></td><td></td></tr><tr><td></td><td></td><td></td></tr></tbody>
  </table>

  <p class="block" style="top:430px;font-weight:600">3.Project Budget</p>
  <table class="data" style="top:478px">
    <thead><tr><th style="width:294px">Project Budget</th><th colspan="2" style="padding-left:14px">Forecast Cost</th><th colspan="2">Real Cost</th></tr></thead>
    <tbody>
      <tr><td></td><td style="width:94px;padding:0 12px">$</td><td style="width:94px;padding:0 14px">Time</td><td style="width:94px;padding:0 14px">$</td><td>Time</td></tr>
      <tr><td></td><td></td><td></td><td></td><td></td></tr><tr><td></td><td></td><td></td><td></td><td></td></tr><tr><td></td><td></td><td></td><td></td><td></td></tr><tr><td></td><td></td><td></td><td></td><td></td></tr><tr><td></td><td></td><td></td><td></td><td></td></tr>
    </tbody>
  </table>

  <p class="block" style="top:748px;font-weight:600">4.Project Milestones Major Tasks</p>
  <table class="data data--compact" style="top:798px">
    <thead><tr><th style="width:166px;padding-left:26px">TASK NAME</th><th style="width:88px">ASSIGNED<br>TO</th><th style="width:80px">START<br>DATE</th><th style="width:148px">END DATE</th><th style="width:90px">DURATION<br>IN DAYS</th><th>STATUS</th></tr></thead>
    <tbody>
      <tr><td style="padding-left:26px">Project Assessment.</td><td>Dana Morrow</td><td></td><td></td><td>$</td><td>Time</td></tr>
      <tr><td></td><td></td><td></td><td></td><td></td><td></td></tr>
    </tbody>
  </table>

  <p class="block" style="top:945px;font-weight:600">Initial Conversation, Collaboration with HR Leadership Team and Senior Management.</p>
  <div class="page-number">03</div>
</section>

</body>
</html>
```